Energy trading company (Voltrisa) needs a business card

We need a business card for a company based in Central America. Our main purpose is trading energy . We already have the logo but we need some good creativity to design a high impact business card. Colors blue, orange, green can be used or we would like to see good combinatios with our logo

Target Market(s)

Energy

Industry/Entity Type

Power Generation

Contact Information for Business Card

Logo , headquarters , name, background

Font styles to use
Serif
Sans Serif

Colors

Designer to choose colors to be used in the design.

Requirements
Must have
• it must have a fresh and clean view
Nice to have
• good backgrounds that combine with the logo
Should not have
• too much words

```html
<!DOCTYPE html>
<html lang="en">
<head>
<meta charset="utf-8">
<title>Voltrisa Business Card</title>
<link rel="stylesheet" href="https://fonts.googleapis.com/css2?family=Lato:wght@400;700&family=Montserrat:wght@700&display=swap">
<style>
  :root {
    --backdrop: #2f302d;
    --card: #151515;
    --card-edge: #0c0c0c;
    --orange: #f08a1c;
    --orange-soft: #e9a24a;
    --white: #ffffff;
    --muted: #d9d9d9;
  }
  * { box-sizing: border-box; margin: 0; padding: 0; }
  html, body {
    width: 1200px; height: 824px; overflow: hidden;
    background: var(--backdrop);
    font-family: "Lato", Arial, sans-serif;
  }
  .canvas {
    position: relative; width: 1200px; height: 824px;
    display: flex; align-items: center; justify-content: center; gap: 60px;
  }
  .card {
    width: 520px; height: 298px;
    background: var(--card);
    border: 1px solid var(--card-edge);
    border-radius: 4px;
    box-shadow: 0 16px 40px rgba(0,0,0,0.45);
    position: relative;
  }
  /* Front */
  .card-front {
    display: flex; flex-direction: column; align-items: center; justify-content: center; gap: 18px;
  }
  .brand-dot {
    width: 44px; height: 44px; border-radius: 50%;
    background: var(--orange);
  }
  .brand-name {
    font-family: "Lato", Arial, sans-serif;
    font-weight: 400; font-size: 54px; letter-spacing: 1px;
    text-transform: uppercase; color: var(--orange);
  }
  /* Back */
  .card-back {
    display: flex; align-items: center; padding: 0 36px 0 44px;
  }
  .back-brand {
    width: 170px; display: flex; flex-direction: column; align-items: center; gap: 10px;
  }
  .back-brand .brand-dot { width: 60px; height: 60px; }
  .back-brand .brand-name { font-size: 26px; letter-spacing: 0.5px; }
  .divider {
    width: 2px; height: 170px; background: var(--orange); margin: 0 26px 0 20px;
  }
  .contact { color: var(--white); }
  .person-name {
    font-family: "Montserrat", Arial, sans-serif; font-weight: 700; font-size: 22px;
  }
  .job-title {
    color: var(--orange-soft); font-size: 13px; letter-spacing: 1px; text-transform: uppercase;
    margin: 2px 0 12px;
  }
  .contact-list { list-style: none; font-size: 14px; line-height: 1.75; }
  .contact-list li { display: flex; align-items: center; gap: 10px; }
  .contact-list svg { width: 13px; height: 13px; fill: none; stroke: var(--orange); stroke-width: 2; }
  .contact-list svg.solid { fill: var(--orange); stroke: none; }
  .address { font-size: 14px; margin-top: 6px; }
</style>
</head>
<body>
<main class="canvas">
  <section class="card card-front" aria-label="Card front">
    <span class="brand-dot"></span>
    <span class="brand-name">Voltrisa</span>
  </section>

  <section class="card card-back" aria-label="Card back">
    <div class="back-brand">
      <span class="brand-dot"></span>
      <span class="brand-name">Voltrisa</span>
    </div>
    <div class="divider"></div>
    <div class="contact">
      <h1 class="person-name">Your Name</h1>
      <p class="job-title">Job Title</p>
      <ul class="contact-list">
        <li>
          <svg class="solid" viewBox="0 0 24 24"><path d="M6.6 10.8a15 15 0 0 0 6.6 6.6l2.2-2.2c.3-.3.7-.4 1-.2 1.1.4 2.3.6 3.6.6.6 0 1 .4 1 1V20c0 .6-.4 1-1 1A17 17 0 0 1 3 4c0-.6.4-1 1-1h3.5c.6 0 1 .4 1 1 0 1.3.2 2.5.6 3.6.1.3 0 .7-.2 1z"/></svg>
          <span>000 000 0000</span>
        </li>
        <li>
          <svg viewBox="0 0 24 24"><rect x="2" y="5" width="20" height="14"/><path d="M2 5l10 8 10-8"/></svg>
          <span>youremai@xyz.com</span>
        </li>
        <li>
          <svg viewBox="0 0 24 24"><circle cx="12" cy="12" r="10"/><path d="M2 12h20M12 2c3 3 3 17 0 20M12 2c-3 3-3 17 0 20"/></svg>
          <span>www.yourwebsite.com</span>
        </li>
      </ul>
      <p class="address">000, Street Name, City, ST 0000</p>
    </div>
  </section>
</main>
</body>
</html>
```